Business Card Design Project

Basketball Training program

Offers: Travel Club Program - Camps - Clinics - Private Training

website: ridgeportcourt.net
Phone Contact: Main Phone: 555-314-7720
Email: ridgeport.court@mailzone.example

Industry/Entity Type

Business

Contact Information for Business Card

Need one for the following coaches:
Marcus Thorne - Boys & Girls Basketball Coach
Kirasol Vendry - Girls Basketball Coach
Anselmo Trujar - Director/Head Coach
Walter Fisk- Boys Basketball
Howard Lindqvist - Boys Basketball
Ramon Etxeberri - Boys Basketball
Talvin Okafor- Boys Basketball/ Trainer
Al Hargrove - Boys & Girls Basketball Coach

Basketball Training program Logo - one side

Logo on the corner
new one on the left (RC)
old one on the right (old one is with the ridgeport and court)

```html
<!DOCTYPE html>
<html lang="en">
<head>
<meta charset="utf-8">
<title>Ridgeport Basketball Training – Business Card</title>
<link href="https://fonts.googleapis.com/css2?family=Tinos:wght@400;700&family=Arimo:wght@400;500&display=swap" rel="stylesheet">
<style>
  :root {
    --stage: #1c1c1c;
    --paper: #f0f0f0;
    --gold: #eaac16;
    --gold-text: #d9a21e;
    --ink: #221f20;
    --white: #ffffff;
    --ghost: #d8d8d8;
    --icon: #8a8a8a;
  }
  * { margin: 0; padding: 0; box-sizing: border-box; }
  html, body { width: 1200px; height: 800px; overflow: hidden; background: var(--stage); }
  .canvas { position: relative; width: 1200px; height: 800px; }
  .card {
    position: absolute; top: 238px; width: 536px; height: 306px;
    background: var(--paper); overflow: hidden;
    box-shadow: 0 6px 18px rgba(0,0,0,.55);
  }
  .card--front { left: 49px; }
  .card--back { left: 617px; }
  .card__bands { position: absolute; inset: 0; }
  .title {
    position: absolute; left: 0; right: 0; top: 52px; text-align: center;
    font-family: "Tinos", "Times New Roman", serif; font-size: 33px; color: var(--ink);
  }
  .brand {
    position: absolute; left: 22px; top: 132px; display: flex; align-items: center; gap: 8px;
  }
  .brand__dot { width: 40px; height: 40px; border-radius: 50%; background: var(--ink); }
  .brand__name {
    font-family: "Tinos", "Times New Roman", serif; font-weight: 700; font-size: 25px; color: var(--ink);
  }
  .mark {
    position: absolute; left: 417px; top: 108px; width: 100px; height: 100px; border-radius: 50%;
    background: var(--white); border: 6px solid var(--ink);
    display: flex; align-items: center; justify-content: center;
    font-family: "Tinos", "Times New Roman", serif; font-weight: 700; font-size: 40px; color: var(--ink);
  }
  .person { position: absolute; left: 16px; top: 226px; color: var(--ink); }
  .person__name { font-family: "Tinos", "Times New Roman", serif; font-size: 27px; line-height: 27px; }
  .person__role { font-family: "Arimo", Arial, sans-serif; font-size: 17.5px; line-height: 20px; }
  .contact {
    position: absolute; right: 16px; top: 223px; list-style: none;
    font-family: "Arimo", Arial, sans-serif; font-size: 13.5px; color: var(--white);
  }
  .contact__item { display: flex; justify-content: flex-end; align-items: center; gap: 10px; height: 22px; }
  .contact__icon { width: 12px; height: 12px; }
  .ghost-mark {
    position: absolute; left: -20px; top: -40px;
    font-family: "Tinos", "Times New Roman", serif; font-weight: 700; font-size: 330px;
    line-height: 1; color: var(--ghost);
  }
  .offers__title {
    position: absolute; right: 30px; top: 52px;
    font-family: "Tinos", "Times New Roman", serif; font-size: 33px; color: var(--gold-text);
  }
  .offers__list {
    position: absolute; right: 28px; top: 119px; list-style: none;
    font-family: "Arimo", Arial, sans-serif; font-weight: 500; font-size: 21px; color: var(--ink);
  }
  .offers__item { display: flex; justify-content: flex-end; align-items: center; gap: 14px; height: 37px; }
  .offers__bullet { width: 14px; height: 14px; }
</style>
</head>
<body>
<main class="canvas">

  <section class="card card--front" aria-label="Card front">
    <svg class="card__bands" width="536" height="306" viewBox="0 0 536 306">
      <polygon points="0,154 222,154 321,299 0,299" fill="var(--gold)"/>
      <polygon points="228,154 536,149 536,299 327,299" fill="var(--ink)"/>
    </svg>
    <h1 class="title">Basketball Training program</h1>
    <div class="brand">
      <span class="brand__dot"></span>
      <span class="brand__name">Ridgeport</span>
    </div>
    <div class="mark">RC</div>
    <div class="person">
      <p class="person__name">Marcus Thorne</p>
      <p class="person__role">Boys &amp; Girls Basketball Coach</p>
    </div>
    <ul class="contact">
      <li class="contact__item">ridgeport.court@mailzone.example
        <svg class="contact__icon" viewBox="0 0 12 12"><rect width="12" height="12" fill="var(--white)"/><rect x="2" y="3.5" width="8" height="5" fill="none" stroke="var(--ink)"/><path d="M2 3.5 L6 6.5 L10 3.5" fill="none" stroke="var(--ink)"/></svg>
      </li>
      <li class="contact__item">ridgeportcourt.net
        <svg class="contact__icon" viewBox="0 0 12 12"><rect width="12" height="12" fill="var(--white)"/><circle cx="6" cy="6" r="3.8" fill="none" stroke="var(--ink)"/><path d="M2.2 6 H9.8 M6 2.2 V9.8" stroke="var(--ink)" stroke-width=".8"/></svg>
      </li>
      <li class="contact__item">555-314-7720
        <svg class="contact__icon" viewBox="0 0 12 12"><rect width="12" height="12" fill="var(--white)"/><rect x="2.5" y="5" width="7" height="4.5" fill="var(--ink)"/><path d="M2 4.5 Q6 1.5 10 4.5" fill="none" stroke="var(--ink)" stroke-width="1.4"/></svg>
      </li>
    </ul>
  </section>

  <section class="card card--back" aria-label="Card back">
    <div class="ghost-mark" aria-hidden="true">RC</div>
    <h2 class="offers__title">Offers :</h2>
    <ul class="offers__list">
      <li class="offers__item">Camps
        <svg class="offers__bullet" viewBox="0 0 14 14"><circle cx="7" cy="7" r="4.5" fill="none" stroke="var(--icon)"/><circle cx="7" cy="7" r="1.6" fill="var(--icon)"/><path d="M7 0 V3 M7 11 V14 M0 7 H3 M11 7 H14" stroke="var(--icon)"/></svg>
      </li>
      <li class="offers__item">Travel Club Program
        <svg class="offers__bullet" viewBox="0 0 14 14"><circle cx="7" cy="7" r="4.5" fill="none" stroke="var(--icon)"/><circle cx="7" cy="7" r="1.6" fill="var(--icon)"/><path d="M7 0 V3 M7 11 V14 M0 7 H3 M11 7 H14" stroke="var(--icon)"/></svg>
      </li>
      <li class="offers__item">Private Training
        <svg class="offers__bullet" viewBox="0 0 14 14"><circle cx="7" cy="7" r="4.5" fill="none" stroke="var(--icon)"/><circle cx="7" cy="7" r="1.6" fill="var(--icon)"/><path d="M7 0 V3 M7 11 V14 M0 7 H3 M11 7 H14" stroke="var(--icon)"/></svg>
      </li>
      <li class="offers__item">Clinics
        <svg class="offers__bullet" viewBox="0 0 14 14"><circle cx="7" cy="7" r="4.5" fill="none" stroke="var(--icon)"/><circle cx="7" cy="7" r="1.6" fill="var(--icon)"/><path d="M7 0 V3 M7 11 V14 M0 7 H3 M11 7 H14" stroke="var(--icon)"/></svg>
      </li>
    </ul>
  </section>

</main>
</body>
</html>
```